GLA

Please send us some options for letterhead I attached our Logo. In addition to the Logo we need this information somewhere on the page

48 Harlow Lane
Linden Falls, VT 06417
555-274-9160

```html
<!DOCTYPE html>
<html lang="en">
<head>
<meta charset="utf-8">
<title>Glenmark Lending Associates – Letterhead</title>
<link href="https://fonts.googleapis.com/css2?family=Arimo:wght@400;700&display=swap" rel="stylesheet">
<style>
  :root {
    --paper: #ffffff;
    --ink-dark: #3a2e2c;
    --band-blue: #1ba6ee;
    --band-cyan: #7cf0ef;
    --band-text: #ffffff;
  }
  html, body {
    margin: 0;
    padding: 0;
    overflow: hidden;
    background: var(--paper);
  }
  .letterhead {
    position: relative;
    width: 927px;
    height: 1200px;
    background: var(--paper);
    font-family: "Arimo", Arial, sans-serif;
    overflow: hidden;
  }
  .brand {
    position: absolute;
    left: 40px;
    top: 38px;
    display: flex;
    align-items: center;
    gap: 22px;
  }
  .brand-mark {
    width: 84px;
    height: 84px;
    background: var(--ink-dark);
  }
  .brand-name {
    margin: 0;
    color: var(--ink-dark);
    font-weight: 700;
    font-size: 20px;
    line-height: 1.2;
  }
  .contact-band {
    position: absolute;
    left: 0;
    bottom: 0;
    width: 100%;
    height: 46px;
    background: linear-gradient(90deg, var(--band-blue) 0%, var(--band-blue) 24%, var(--band-cyan) 47%, var(--band-blue) 76%, var(--band-blue) 100%);
    display: flex;
    align-items: center;
    justify-content: center;
  }
  .contact-line {
    margin: 0;
    color: var(--band-text);
    font-size: 16px;
    font-weight: 400;
    display: flex;
    gap: 24px;
    align-items: center;
    white-space: nowrap;
  }
  .contact-sep {
    font-size: 18px;
  }
</style>
</head>
<body>
  <main class="letterhead">
    <header class="brand">
      <div class="brand-mark"></div>
      <p class="brand-name">Glenmark<br>Lending Associates</p>
    </header>

    <footer class="contact-band">
      <p class="contact-line">
        <span class="contact-street">48 Harlow Lane</span>
        <span class="contact-sep">|</span>
        <span class="contact-city">Linden Falls, VT 06417</span>
        <span class="contact-sep">|</span>
        <span class="contact-phone">555-274-9160</span>
      </p>
    </footer>
  </main>
</body>
</html>
```